Professional individual needs business card design

I need a business card designed for my friend to show their skills and contact details

I would like to see pattern designs with a black foreground and strong look - will submit content specifics but basics are:

NAME SURNAME (large and bold)
Event Manager & MC

Velvet Harbour
The other event I run

phone number - email

```html
<!DOCTYPE html>
<html lang="en">
<head>
<meta charset="utf-8">
<title>John Doe – Business Card</title>
<link rel="stylesheet" href="https://fonts.googleapis.com/css2?family=Oswald:wght@200;700&family=Lato:wght@400&display=swap">
<style>
  :root {
    --backdrop: #2b2b2b;
    --card: #1c1c1d;
    --card-line: rgba(255,255,255,0.025);
    --ink-strong: #e6e6e6;
    --ink-soft: #bdbdbd;
    --accent: #d3222a;
  }
  html, body {
    margin: 0;
    padding: 0;
    width: 1200px;
    height: 716px;
    overflow: hidden;
    background: var(--backdrop);
  }
  .canvas {
    position: relative;
    width: 1200px;
    height: 716px;
  }
  .card {
    position: absolute;
    left: 425px;
    top: 52px;
    width: 350px;
    height: 612px;
    border-radius: 22px;
    background:
      repeating-linear-gradient(135deg, var(--card-line) 0 1px, transparent 1px 4px),
      var(--card);
    box-shadow: 0 14px 40px rgba(0,0,0,0.45);
    overflow: hidden;
  }
  .brand {
    position: absolute;
    right: 30px;
    top: 72px;
    display: flex;
    align-items: center;
    gap: 10px;
    font-family: 'Lato', sans-serif;
    font-size: 15px;
    color: var(--ink-strong);
  }
  .brand-dot {
    width: 14px;
    height: 14px;
    border-radius: 50%;
    background: var(--accent);
  }
  .name {
    position: absolute;
    left: 34px;
    top: 150px;
    margin: 0;
    font-family: 'Oswald', sans-serif;
    line-height: 0.95;
    font-size: 48px;
    text-transform: uppercase;
    letter-spacing: 0.5px;
  }
  .name-first { display: block; font-weight: 700; color: var(--ink-strong); }
  .name-last { display: block; font-weight: 200; color: var(--ink-soft); }
  .roles {
    position: absolute;
    left: 152px;
    top: 196px;
    margin: 0;
    font-family: 'Lato', sans-serif;
    font-size: 15px;
    line-height: 1.45;
    color: var(--accent);
  }
  .contact {
    position: absolute;
    display: flex;
    align-items: flex-start;
    gap: 12px;
    font-family: 'Lato', sans-serif;
    font-size: 14px;
    color: var(--ink-strong);
    white-space: nowrap;
  }
  .contact-bar {
    width: 4px;
    height: 78px;
    background: var(--accent);
    margin-top: 2px;
  }
  .contact-body { display: flex; align-items: center; gap: 10px; }
  .contact-icon { width: 18px; height: 18px; fill: var(--accent); flex: none; }
  .contact-phone { left: 96px; top: 300px; }
  .contact-email { left: 136px; top: 440px; }
</style>
</head>
<body>
<main class="canvas">
  <article class="card">
    <div class="brand">
      <span class="brand-dot"></span>
      <span class="brand-name">Velvet Harbour</span>
    </div>

    <h1 class="name">
      <span class="name-first">John</span>
      <span class="name-last">Doe</span>
    </h1>

    <p class="roles">Event Manager &amp; MC<br>Velvet Harbour</p>

    <div class="contact contact-phone">
      <span class="contact-bar"></span>
      <span class="contact-body">
        <svg class="contact-icon" viewBox="0 0 24 24" aria-hidden="true">
          <path d="M3 8c0-2 2-3 9-3s9 1 9 3v2h-5V8H8v2H3z"/>
          <path d="M6 12h12l2 7H4z"/>
        </svg>
        000 000 0000
      </span>
    </div>

    <div class="contact contact-email">
      <span class="contact-bar"></span>
      <span class="contact-body">
        <svg class="contact-icon" viewBox="0 0 24 24" aria-hidden="true">
          <path d="M2 5h20v14H2z M3.5 6.5 12 13l8.5-6.5" fill="var(--accent)" stroke="var(--card)" stroke-width="1.5"/>
        </svg>
        hello@velvetharbour.net
      </span>
    </div>
  </article>
</main>
</body>
</html>
```